Calm Fern Healthcare- Aged Care and Community Services

Looking for brochure to advertise our services. I will attach a draft that we do not want to use. Looking for graphics that are as natural as possible to present a personalised service. We supply services to aged people and people with disability. Please make it look classy and professional at the same time. I am looking for creativity. I have also attached the logo. Site addresses can be the last page. ideally looking for 2 designs, one A4 and another smaller possibly DL. Looking for creative out of the box thinkers. Thank you.

Target Market(s)

Aged Care service providers, disability service providers and private hospitals

Font styles to use
Serif
Sans Serif
Script

Colors
6b449b
886aae
eea4c8
f59195
fac994
3176b5
0555a3
cedeed
e4daeb

Requirements
Must have
• Targeted imagery, content and contact details
Nice to have
• personal profiles of people happy with our services

```html
<!DOCTYPE html>
<html lang="en">
<head>
<meta charset="utf-8">
<title>Calm Fern Healthcare – Booklet</title>
<link href="https://fonts.googleapis.com/css2?family=Montserrat:wght@400;600;700;800&family=Nunito+Sans:wght@300;400;600&display=swap" rel="stylesheet">
<style>
:root{
  --purple:#6b449b;
  --lavender:#886aae;
  --lilac:#e4daeb;
  --pink:#eea4c8;
  --salmon:#f59195;
  --peach:#fac994;
  --sky:#cedeed;
  --label-grey:#d1d2d4;
  --white:#ffffff;
}
*{margin:0;padding:0;box-sizing:border-box}
html,body{width:1200px;height:849px;overflow:hidden;background:var(--white)}
body{font-family:"Nunito Sans",Arial,sans-serif;color:var(--purple)}
.canvas{position:relative;width:1200px;height:849px;overflow:hidden}
.board{position:absolute;left:0;top:0;width:2280px;height:1613px;overflow:hidden;transform:scale(0.526316);transform-origin:0 0}
.page{position:absolute;background:var(--white);overflow:hidden;box-shadow:3px 4px 8px rgba(0,0,0,.28)}
.page svg.shapes{position:absolute;left:0;top:0;width:100%;height:100%}
.abs{position:absolute}
.photo-fill{fill:url(#warm)}
h2{font-family:"Montserrat",sans-serif;font-weight:700;font-size:12.5px;letter-spacing:.3px;color:var(--purple);text-transform:uppercase;margin-bottom:5px}
.body-text{font-size:6.3px;line-height:1.33;color:var(--purple)}
.body-text p{margin-bottom:7px}
.body-text .sub{text-transform:uppercase;display:block}
.list{list-style:none;font-size:6.3px;color:var(--purple)}
.list li{margin-bottom:9px;padding-left:8px;position:relative}
.list li::before{content:"";position:absolute;left:0;top:2px;width:3px;height:3px;border-radius:50%;background:var(--purple)}
.brand-name{font-family:"Montserrat",sans-serif;font-weight:600;color:var(--purple);display:flex;align-items:center;gap:8px}
.brand-dot{width:14px;height:14px;border-radius:50%;background:var(--purple);flex:none}

/* front cover */
.cover-front{left:174px;top:212px;width:472px;height:676px;transform:rotate(-2.3deg)}
.cover-title{left:248px;top:552px;font-family:"Montserrat",sans-serif;font-weight:700;font-size:25px;line-height:1.08;color:var(--purple);white-space:nowrap}
.cover-url{left:250px;top:626px;font-family:"Montserrat",sans-serif;font-weight:700;font-size:10px;color:var(--purple);white-space:nowrap}
.cover-brand{left:44px;top:590px;font-size:15px;width:180px;line-height:1.15}

/* back cover */
.cover-back{left:472px;top:368px;width:521px;height:745px;box-shadow:3px 4px 8px rgba(0,0,0,.22)}
.back-brand{left:190px;top:410px;font-size:15px;width:160px;line-height:1.15}
.contact{font-family:"Montserrat",sans-serif;font-size:9.5px;line-height:1.28;color:var(--white)}
.contact .lbl{font-weight:400}
.contact .val{font-weight:600}

/* label */
.label{position:absolute;left:365px;top:1285px;width:425px;height:328px;background:var(--label-grey)}
.label h1{position:absolute;left:45px;top:58px;font-family:"Montserrat",sans-serif;font-weight:800;font-size:44px;line-height:.98;color:var(--white);letter-spacing:.5px}
.label p{position:absolute;left:45px;top:183px;font-family:"Nunito Sans",sans-serif;font-weight:300;font-size:26px;color:var(--white)}

/* spreads */
.spread{left:1273px;width:669px;height:474px}
.spread-1{top:70px}
.spread-2{top:575px}
.spread-3{top:1080px}
.callout{font-family:"Montserrat",sans-serif;font-weight:700;font-size:6.3px;line-height:1.35;color:var(--white);text-transform:uppercase}
.on-purple h2,.on-purple .body-text{color:var(--white)}
.quote{font-family:"Montserrat",sans-serif;font-weight:600;font-size:10.5px;line-height:1.3;color:var(--purple)}
.quote small{display:block;font-family:"Nunito Sans",sans-serif;font-weight:400;font-size:5.5px;text-align:right}
</style>
</head>
<body>
<svg width="0" height="0" style="position:absolute">
  <defs>
    <linearGradient id="warm" x1="0" y1="0" x2="1" y2="1">
      <stop offset="0" stop-color="#e8d6bf"/>
      <stop offset=".5" stop-color="#b9a08a"/>
      <stop offset="1" stop-color="#7ea6c9"/>
    </linearGradient>
    <linearGradient id="staff" x1="0" y1="0" x2="0" y2="1">
      <stop offset="0" stop-color="#e6e8ea"/>
      <stop offset="1" stop-color="#4f6f96"/>
    </linearGradient>
    <linearGradient id="garden" x1="0" y1="0" x2="1" y2="1">
      <stop offset="0" stop-color="#c5d7a9"/>
      <stop offset="1" stop-color="#8fb3d6"/>
    </linearGradient>
    <linearGradient id="lounge" x1="0" y1="0" x2="1" y2="1">
      <stop offset="0" stop-color="#d9d3c9"/>
      <stop offset=".6" stop-color="#a7c4c0"/>
      <stop offset="1" stop-color="#5777b0"/>
    </linearGradient>
  </defs>
</svg>

<div class="canvas">
<main class="board">

  <!-- back cover -->
  <section class="page cover-back">
    <svg class="shapes" viewBox="0 0 521 745" preserveAspectRatio="none">
      <polygon points="0,592 521,505 521,745 0,745" fill="var(--purple)"/>
      <g fill="none" stroke="var(--lavender)" stroke-width="3" opacity=".55">
        <path d="M45,610 c-30,20 -25,70 20,110 c45,40 95,55 115,30 l12,-16 c5,-8 2,-16 -6,-20 l-30,-16 c-8,-4 -16,-2 -20,5 l-8,12 c-20,-6 -50,-36 -56,-56 l12,-8 c7,-4 9,-12 5,-20 l-16,-30 c-4,-8 -12,-11 -20,-6 z"/>
        <path d="M120,600 a50,50 0 0 1 50,50"/>
        <path d="M120,580 a70,70 0 0 1 70,70"/>
      </g>
    </svg>
    <div class="abs brand-name back-brand"><span class="brand-dot"></span>Calm Fern Healthcare</div>
    <div class="abs contact" style="left:317px;top:594px">
      <span class="lbl">ADDRESS</span>
    </div>
    <div class="abs contact" style="left:372px;top:594px">
      <div class="val">14 Wattle Lane<br>Ashvale WA 6199<br>Australia</div>
      <div class="val" style="margin-top:13px">Ground Floor,<br>58 Harbour Street<br>Brookdale SA 5099<br>Australia</div>
    </div>
    <div class="abs contact" style="left:72px;top:653px">
      <div class="lbl">PHONE<br>WEB<br>EMAIL</div>
    </div>
    <div class="abs contact" style="left:127px;top:653px">
      <div class="val">(08) 9000 4172<br>calmfernhealthcare.com.au<br>hello@calmfernhealthcare.com.au</div>
    </div>
  </section>

  <!-- front cover -->
  <section class="page cover-front">
    <svg class="shapes" viewBox="0 0 472 676" preserveAspectRatio="none">
      <rect width="472" height="676" fill="var(--purple)"/>
      <polygon class="photo-fill" points="130,0 472,0 472,432 213,502" role="img" aria-label="Photo of a carer holding an elderly client's hands"/>
      <polygon points="0,556 472,430 472,676 0,676" fill="var(--white)"/>
    </svg>
    <div class="abs brand-name cover-brand"><span class="brand-dot"></span>Calm Fern Healthcare</div>
    <div class="abs cover-title">REIMAGINING<br>HEALTHCARE</div>
    <div class="abs cover-url">CALMFERNHEALTHCARE.COM.AU</div>
  </section>

  <!-- label -->
  <aside class="label">
    <h1>CALM FERN<br>HEALTHCARE</h1>
    <p>Booklet, Double Sided</p>
  </aside>

  <!-- spread 1 -->
  <section class="page spread spread-1">
    <svg class="shapes" viewBox="0 0 669 474" preserveAspectRatio="none">
      <polygon points="0,0 14,0 26,474 0,474" fill="var(--purple)"/>
      <polygon points="14,415 262,458 255,474 16,474" fill="var(--sky)"/>
      <polygon points="298,474 318,448 669,385 669,474" fill="var(--pink)"/>
      <rect x="47" y="68" width="250" height="142" rx="14" fill="url(#staff)" stroke="var(--lavender)" stroke-width="3" role="img" aria-label="Group photo of smiling care staff in uniform"/>
      <polygon points="380,355 568,363 568,445 380,445" fill="var(--purple)"/>
    </svg>
    <div class="abs" style="left:45px;top:240px;width:255px">
      <h2>About Us</h2>
      <div class="body-text">
        <p>Calm Fern Healthcare is a Perth based staffing solutions provider which helps partner organisations meet their ongoing resource needs. We are building a name for our quick response to client enquiries while meeting our key service goals. We work with providers in Residential Aged Care, Community Supports and Hospitals.</p>
        <p>We believe the key to lasting relationships is willingness and the ability to give back, which we aim to do by understanding the needs of our clients, solving problems together, helping them move forward and earning trust.</p>
        <p>Our vision is to be the most responsive staffing provider in WA, sourcing and placing staff who hold strong values such as ethics, accountability, respect, integrity and adaptability. Our mission is to partner with like-minded organisations that truly want to make a difference and hold good care governance.</p>
      </div>
    </div>
    <div class="abs" style="left:380px;top:68px;width:270px">
      <h2>Who We Employ</h2>
      <div class="body-text">
        <p>We actively source and recruit skilled professionals<br>with a direct cultural fit for most of our clients.</p>
        <p>These roles include but are not limited to:</p>
      </div>
      <ul class="list">
        <li>Registered Nurses</li>
        <li>Enrolled Nurses</li>
        <li>Nursing Assistants/Carers</li>
        <li>Allied Health Assistants (Physiotherapy &amp; OT)</li>
        <li>Chefs and Cooks (healthcare experienced)</li>
        <li>Catering Staff and Kitchen Hands</li>
        <li>Cleaning and Domestic Assistants</li>
        <li>Laundry Attendants</li>
      </ul>
      <div class="body-text" style="padding-left:8px">...and many more professionals.</div>
    </div>
    <div class="abs" style="left:380px;top:282px;width:270px">
      <h2>What We Believe</h2>
      <div class="body-text">
        <p>A person who is valued always does more than what is expected.</p>
        <p>Our staff are at the centre of all our decisions as we are only as good as the people we hire. If we look after our staff, they will look after our clients.</p>
      </div>
    </div>
    <div class="abs callout" style="left:401px;top:385px;width:150px">Our diverse database of skilled staff gives you the peace of mind you need to do what you do best, to look after your customers.</div>
  </section>

  <!-- spread 2 -->
  <section class="page spread spread-2">
    <svg class="shapes" viewBox="0 0 669 474" preserveAspectRatio="none">
      <polygon points="0,474 669,372 669,474" fill="var(--salmon)" opacity=".65"/>
      <polygon points="0,287 298,287 298,422 0,470" fill="url(#garden)" role="img" aria-label="Photo of a nurse greeting a smiling elderly woman outdoors"/>
      <polygon points="373,190 640,218 640,474 373,474" fill="var(--purple)"/>
    </svg>
    <div class="abs" style="left:45px;top:55px;width:258px">
      <h2>Why Partner With Us</h2>
      <div class="body-text">
        <p><span class="sub">Service Design</span>Before placing any staff, we complete a full client profile to understand your business needs, end-to-end operations, service delivery, HR and governance.</p>
        <p>This lets us design a service around your specific needs which allows for a seamless integration.</p>
        <p>We encourage continuity of service by placing the same staff at your sites. This lets our staff build real relationships with your team and customers for a perfect fit.</p>
        <p><span class="sub">Technology</span>We have brought in the systems and technology we believe are part of modern day efficiencies.</p>
        <p>People are our business and nothing can replace human relationships and connection, however technology helps us make the most of these efficiencies and keep errors low.</p>
        <p>Our on-boarding and scheduling platforms are automated, further improving compliance and managing risk.</p>
      </div>
    </div>
    <div class="abs" style="left:381px;top:55px;width:260px">
      <h2>Key Partnership Benefits</h2>
      <div class="body-text">
        <p><span class="sub">Financial</span>A partnership with Calm Fern will improve your margins and profits, letting you put more money towards plans that enable operational excellence.</p>
        <p><span class="sub">Service Delivery Improvements</span>Enhanced customer choice and flexibility as well as improved customer outcomes.</p>
        <p><span class="sub">Risk Management Enhancements</span>You have the option of outsourcing workforce and cost.</p>
        <p><span class="sub">Operational Efficiencies</span>Improved organisational efficiencies and best use of the workforce.</p>
      </div>
    </div>
    <div class="abs on-purple" style="left:381px;top:235px;width:255px">
      <h2>The Real Return of Investment</h2>
      <div class="body-text">
        <p><span class="sub">Patient Satisfaction</span>The more your clients are satisfied, the more they will promote your brand, speaking highly of your service delivery during accreditation and, in the end, the more they feel you value them as individuals.</p>
        <p>The national care standards body keeps seeking evidence of caring, compliant and effective corporate and clinical governance. By building these standards into each policy, process and service from setup to review, you can rest easy should any regulator decide to pay you a visit.</p>
        <p>We are here to ensure we align to your standard while staying adaptable to the changing nature of the industry we operate in.</p>
      </div>
    </div>
  </section>

  <!-- spread 3 -->
  <section class="page spread spread-3">
    <svg class="shapes" viewBox="0 0 669 474" preserveAspectRatio="none">
      <polygon points="0,385 372,474 0,474" fill="var(--peach)"/>
      <rect x="336" y="0" width="333" height="474" fill="url(#lounge)" role="img" aria-label="Photo of a carer sitting with a laughing elderly woman in a lounge"/>
      <polygon points="483,340 640,300 640,474 483,474" fill="var(--purple)"/>
    </svg>
    <div class="abs" style="left:45px;top:58px;width:270px">
      <h2>Redesigning Resident Experiences</h2>
      <div class="body-text">We value feedback and we constantly seek it as it helps us grow.<br>Service delivery and feedback are a match that cannot be undone.</div>
    </div>
    <div class="abs quote" style="left:45px;top:119px">“Feedback type one can go here”<small>- Ana Rees, Calm Fern Nurse</small></div>
    <div class="abs quote" style="left:124px;top:158px;width:155px">“Longer type feedback two can be placed here that has three to four lines of text”<small>- Ana Rees, Calm Fern Nurse</small></div>
    <div class="abs quote" style="left:45px;top:226px;width:200px">“Feedback type three can go here that has a long sentence about you”<small>- Tom Hale, Aged Care Resident</small></div>
    <div class="abs" style="left:45px;top:288px;width:230px">
      <h2>Retaining Customers and<br>How We Grow</h2>
      <ul class="list" style="margin-top:4px">
        <li>Ensure positive first encounters</li>
        <li>Maintain professionalism</li>
        <li>Continue training and development</li>
      </ul>
    </div>
    <div class="abs on-purple" style="left:501px;top:353px;width:132px">
      <h2 style="font-size:10.5px;margin-bottom:4px">The Vision</h2>
      <div class="callout">Our vision is to be the most responsive staff solutions provider in Western Australia, while sourcing and placing staff that hold strong values which include ethics, accountability, respect, integrity and adaptability.</div>
    </div>
  </section>

</main>
</div>
</body>
</html>
```